Marlow Sky Charter E-mail Signature

Need to create an email signature for Marlow Sky Charter. Signature should include the Marlow logo and the associated QFTR member logo

```html
<!DOCTYPE html>
<html lang="en">
<head>
<meta charset="utf-8">
<title>Marlow Sky Charter – E-mail Signature Options</title>
<link href="https://fonts.googleapis.com/css2?family=Montserrat:wght@400;500;600;700&display=swap" rel="stylesheet">
<style>
  :root {
    --board: #cbc6c3;
    --panel: #ffffff;
    --brand-blue: #1565c0;
    --ink: #1f1f1f;
    --muted: #444444;
    --rule: #1565c0;
    --label-bg: #2f2f2f;
    --label-ink: #ffffff;
  }
  * { box-sizing: border-box; margin: 0; padding: 0; }
  html, body { width: 1200px; height: 867px; overflow: hidden; }
  body {
    background: var(--board);
    font-family: "Montserrat", sans-serif;
    position: relative;
  }
  .option {
    position: absolute;
    width: 367px;
    height: 257px;
  }
  .option__panel {
    position: absolute;
    left: 50px; top: 8px;
    width: 260px; height: 214px;
    background: var(--panel);
    box-shadow: 0 2px 6px rgba(0,0,0,.12);
  }
  .option__label {
    position: absolute;
    left: 306px; top: 234px;
    width: 61px; height: 20px;
    background: var(--label-bg);
    color: var(--label-ink);
    font-size: 8px; font-weight: 600;
    letter-spacing: .3px;
    display: flex; align-items: center; justify-content: center;
  }
  .signature {
    position: absolute;
    left: 55px; top: 100px;
    width: 249px; height: 70px;
  }
  .signature__bar {
    position: absolute;
    left: 0; top: 66px;
    width: 249px; height: 4px;
    background: var(--rule);
  }
  .brand {
    position: absolute;
    left: 15px;
    width: 52px;
    display: flex; align-items: center; gap: 3px;
    transform: translateY(-50%);
    color: var(--brand-blue);
    font-size: 6.4px; font-weight: 700;
    line-height: 7px;
  }
  .brand__dot { flex: none; width: 6px; height: 6px; border-radius: 50%; background: var(--brand-blue); }
  .brand__name { display: block; white-space: nowrap; }
  .divider { position: absolute; width: 1px; background: var(--brand-blue); }
  .person__name { position: absolute; font-weight: 700; color: var(--brand-blue); font-size: 8px; white-space: nowrap; }
  .person__title { position: absolute; font-weight: 700; color: var(--ink); font-size: 3.6px; letter-spacing: .2px; text-transform: uppercase; white-space: nowrap; }
  .contact { position: absolute; font-size: 3.8px; line-height: 5.6px; color: var(--ink); white-space: nowrap; }
  .socials { position: absolute; display: flex; gap: 3px; }
  .socials span { width: 7px; height: 7px; border-radius: 50%; background: var(--brand-blue); }
  .member { position: absolute; display: flex; align-items: center; gap: 2px; color: var(--ink); font-weight: 600; font-size: 6px; letter-spacing: .5px; }
  .member__dot { width: 7px; height: 5px; border-radius: 50%; background: var(--brand-blue); }
  .member__note { position: absolute; top: -4px; left: 12px; font-size: 2.4px; font-weight: 400; letter-spacing: 0; white-space: nowrap; }

  .signature--stacked .person__name { color: var(--ink); }
  .signature--stacked .person__title { font-weight: 500; text-transform: none; font-size: 4.4px; letter-spacing: 0; color: var(--muted); }
  .signature--stacked .underline { position: absolute; height: .5px; width: 58px; background: #bbbbbb; }
  .signature--stacked .member { font-size: 8px; }
  .signature--stacked .member__dot { width: 10px; height: 7px; }
  .signature--stacked .member__note { left: 14px; top: -4px; }
</style>
</head>
<body>

<section class="option" style="left:25px;top:29px">
  <div class="option__panel"></div>
  <div class="signature">
    <div class="brand" style="top:29px"><span class="brand__dot"></span><span><span class="brand__name">Marlow Sky</span><span class="brand__name">Charter</span></span></div>
    <div class="divider" style="left:77px;top:2px;height:53px"></div>
    <div class="person__name" style="left:90px;top:9px">Ross Calder</div>
    <div class="person__title" style="left:90px;top:21px">Marketing Expert</div>
    <div class="socials" style="left:90px;top:40px"><span></span><span></span><span></span><span></span></div>
    <div class="divider" style="left:164px;top:2px;height:53px"></div>
    <div class="contact" style="left:180px;top:8px">p : (555) 010-4821<br>f : (555) 010-7390<br>e : rcalder@marlowsky.com<br>w : www.marlowsky.com</div>
    <div class="member" style="left:180px;top:40px"><span class="member__dot"></span>QFTR<span class="member__note">member of</span></div>
    <div class="signature__bar"></div>
  </div>
  <div class="option__label">OPTION 01</div>
</section>

<section class="option" style="left:412px;top:29px">
  <div class="option__panel"></div>
  <div class="signature">
    <div class="brand" style="top:19px"><span class="brand__dot"></span><span><span class="brand__name">Marlow Sky</span><span class="brand__name">Charter</span></span></div>
    <div class="divider" style="left:77px;top:2px;height:53px"></div>
    <div class="person__name" style="left:90px;top:9px">Ross Calder</div>
    <div class="person__title" style="left:90px;top:21px">Marketing Expert</div>
    <div class="socials" style="left:90px;top:40px"><span></span><span></span><span></span><span></span></div>
    <div class="divider" style="left:164px;top:2px;height:53px"></div>
    <div class="contact" style="left:180px;top:8px">p : (555) 010-4821<br>f : (555) 010-7390<br>e : rcalder@marlowsky.com<br>w : www.marlowsky.com</div>
    <div class="member" style="left:180px;top:40px"><span class="member__dot"></span>QFTR<span class="member__note">member of</span></div>
    <div class="signature__bar"></div>
  </div>
  <div class="option__label">OPTION 02</div>
</section>

<section class="option" style="left:803px;top:29px">
  <div class="option__panel"></div>
  <div class="signature">
    <div class="brand" style="top:41px"><span class="brand__dot"></span><span><span class="brand__name">Marlow Sky</span><span class="brand__name">Charter</span></span></div>
    <div class="divider" style="left:77px;top:2px;height:53px"></div>
    <div class="person__name" style="left:90px;top:9px">Ross Calder</div>
    <div class="person__title" style="left:90px;top:21px">Marketing Expert</div>
    <div class="socials" style="left:90px;top:40px"><span></span><span></span><span></span><span></span></div>
    <div class="divider" style="left:164px;top:2px;height:53px"></div>
    <div class="contact" style="left:180px;top:8px">p : (555) 010-4821<br>f : (555) 010-7390<br>e : rcalder@marlowsky.com<br>w : www.marlowsky.com</div>
    <div class="member" style="left:180px;top:40px"><span class="member__dot"></span>QFTR<span class="member__note">member of</span></div>
    <div class="signature__bar"></div>
  </div>
  <div class="option__label">OPTION 03</div>
</section>

<section class="option" style="left:25px;top:303px">
  <div class="option__panel"></div>
  <div class="signature signature--stacked">
    <div class="brand" style="top:31px"><span class="brand__dot"></span><span><span class="brand__name">Marlow Sky</span><span class="brand__name">Charter</span></span></div>
    <div class="divider" style="left:74px;top:14px;height:32px"></div>
    <div class="person__name" style="left:86px;top:9px">Ross Calder</div>
    <div class="person__title" style="left:86px;top:19px">Director of Aviation</div>
    <div class="underline" style="left:86px;top:25px"></div>
    <div class="contact" style="left:86px;top:27px">p : (555) 010-4821<br>f : (555) 010-7390<br>e : rcalder@marlowsky.com<br>w : www.marlowsky.com</div>
    <div class="divider" style="left:174px;top:14px;height:32px"></div>
    <div class="member" style="left:187px;top:21px"><span class="member__dot"></span>QFTR<span class="member__note">member of</span></div>
    <div class="socials" style="left:188px;top:34px"><span></span><span></span><span></span><span></span></div>
    <div class="signature__bar"></div>
  </div>
  <div class="option__label">OPTION 04</div>
</section>

<section class="option" style="left:412px;top:303px">
  <div class="option__panel"></div>
  <div class="signature signature--stacked">
    <div class="brand" style="top:40px"><span class="brand__dot"></span><span><span class="brand__name">Marlow Sky</span><span class="brand__name">Charter</span></span></div>
    <div class="divider" style="left:74px;top:14px;height:32px"></div>
    <div class="person__name" style="left:86px;top:6px">Ross Calder</div>
    <div class="person__title" style="left:86px;top:16px">Director of Aviation</div>
    <div class="underline" style="left:86px;top:22px"></div>
    <div class="contact" style="left:86px;top:24px">p : (555) 010-4821<br>f : (555) 010-7390<br>e : rcalder@marlowsky.com<br>w : www.marlowsky.com</div>
    <div class="divider" style="left:174px;top:14px;height:32px"></div>
    <div class="member" style="left:187px;top:21px"><span class="member__dot"></span>QFTR<span class="member__note">member of</span></div>
    <div class="socials" style="left:188px;top:34px"><span></span><span></span><span></span><span></span></div>
    <div class="signature__bar"></div>
  </div>
  <div class="option__label">OPTION 05</div>
</section>

<section class="option" style="left:25px;top:578px">
  <div class="option__panel"></div>
  <div class="signature">
    <div class="brand" style="top:34px"><span class="brand__dot"></span><span><span class="brand__name">Marlow Sky</span><span class="brand__name">Charter</span></span></div>
    <div class="person__name" style="left:90px;top:11px">Ross Calder</div>
    <div class="person__title" style="left:90px;top:23px">Director of Aviation</div>
    <div class="socials" style="left:90px;top:42px"><span></span><span></span><span></span><span></span></div>
    <div class="contact" style="left:180px;top:10px">p : (555) 010-4821<br>f : (555) 010-7390<br>e : rcalder@marlowsky.com<br>w : www.marlowsky.com</div>
    <div class="member" style="left:180px;top:45px"><span class="member__dot"></span>QFTR<span class="member__note">member of</span></div>
    <div class="signature__bar"></div>
  </div>
  <div class="option__label">OPTION 06</div>
</section>

<section class="option" style="left:412px;top:578px">
  <div class="option__panel"></div>
  <div class="signature">
    <div class="brand" style="top:46px"><span class="brand__dot"></span><span><span class="brand__name">Marlow Sky</span><span class="brand__name">Charter</span></span></div>
    <div class="person__name" style="left:90px;top:14px">Ross Calder</div>
    <div class="person__title" style="left:90px;top:26px">Director of Aviation</div>
    <div class="socials" style="left:90px;top:42px"><span></span><span></span><span></span><span></span></div>
    <div class="contact" style="left:180px;top:13px">p : (555) 010-4821<br>f : (555) 010-7390<br>e : rcalder@marlowsky.com<br>w : www.marlowsky.com</div>
    <div class="member" style="left:180px;top:42px"><span class="member__dot"></span>QFTR<span class="member__note">member of</span></div>
    <div class="signature__bar"></div>
  </div>
  <div class="option__label">OPTION 07</div>
</section>

<section class="option" style="left:803px;top:578px">
  <div class="option__panel"></div>
  <div class="signature">
    <div class="brand" style="top:22px"><span class="brand__dot"></span><span><span class="brand__name">Marlow Sky</span><span class="brand__name">Charter</span></span></div>
    <div class="person__name" style="left:90px;top:11px">Ross Calder</div>
    <div class="person__title" style="left:90px;top:23px">Director of Aviation</div>
    <div class="socials" style="left:90px;top:42px"><span></span><span></span><span></span><span></span></div>
    <div class="contact" style="left:180px;top:10px">p : (555) 010-4821<br>f : (555) 010-7390<br>e : rcalder@marlowsky.com<br>w : www.marlowsky.com</div>
    <div class="member" style="left:180px;top:45px"><span class="member__dot"></span>QFTR<span class="member__note">member of</span></div>
    <div class="signature__bar"></div>
  </div>
  <div class="option__label">OPTION 08</div>
</section>

</body>
</html>
```